Car Wrap Design for Solar Energy Company

We are company that sell and install solar systems and components. We have three Velmo Trask cars and one Kovini Pelder open back van. We are looking to crate a cool car design that we can use for all our vehicles now and in the future. We are looking more for a whole design, instead of separate elements. It would be nice if its, something that can work on future cars that are different than the ones now.

Target Market(s)

Domestic

Industry/Entity Type

Solar Energy

Font styles to use
Sans Serif

Colors
0054AA
0677BA
7BADD7
CADEEF
E8F1F8
59FF00
82FF00
B8FF75
E3FFCB
F4FFEA
FFF300
FFF600
FEFA6F
FFFEC7
FFFEE8
F0912C
F2A743
F7CA91
FBE8D2
FDF5EE

Requirements
Must have
• The logo, website, phone, socials

```html
<!DOCTYPE html>
<html lang="en">
<head>
<meta charset="utf-8">
<title>Sunvale – Vehicle Wrap Side Panel</title>
<link rel="stylesheet" href="https://fonts.googleapis.com/css2?family=Montserrat:wght@500;600;700&display=swap">
<style>
  :root {
    --canvas-bg: #ececec;
    --panel-white: #ffffff;
    --brand-grey: #555b66;
    --brand-yellow: #f2b632;
    --brand-blue: #2f9fe6;
    --brand-blue-mid: #5fb6ec;
    --brand-blue-light: #9fcdf0;
    --brand-blue-pale: #e3f1fb;
    --text-dark: #3a3f48;
  }
  html, body {
    margin: 0;
    padding: 0;
    width: 1200px;
    height: 1000px;
    overflow: hidden;
    background: var(--canvas-bg);
    font-family: "Montserrat", sans-serif;
  }
  .canvas {
    position: relative;
    width: 1200px;
    height: 1000px;
  }
  .wrap-panel {
    position: absolute;
    left: 60px;
    top: 270px;
    width: 1080px;
    height: 440px;
    background: var(--panel-white);
    border-radius: 28px;
    overflow: hidden;
    box-shadow: 0 2px 10px rgba(0,0,0,0.08);
  }
  .wrap-graphics {
    position: absolute;
    inset: 0;
    width: 100%;
    height: 100%;
  }
  .brand-block {
    position: absolute;
    left: 470px;
    top: 62px;
    display: flex;
    flex-direction: column;
    align-items: flex-start;
  }
  .brand-name {
    display: flex;
    align-items: center;
    gap: 18px;
    margin: 0 0 16px;
  }
  .brand-dot {
    width: 54px;
    height: 54px;
    border-radius: 50%;
    background: var(--brand-yellow);
    flex: none;
  }
  .brand-wordmark {
    font-weight: 600;
    font-size: 70px;
    letter-spacing: 1px;
    line-height: 1;
    color: var(--brand-grey);
  }
  .contact-stack {
    display: inline-flex;
    flex-direction: column;
    align-items: flex-end;
  }
  .contact-website {
    font-weight: 600;
    font-size: 38px;
    color: var(--brand-grey);
    margin: 0;
    line-height: 1.15;
  }
  .contact-social {
    margin: 4px 0 0;
    font-weight: 700;
    font-size: 17px;
    line-height: 1.2;
    color: var(--text-dark);
    display: flex;
    align-items: center;
    gap: 7px;
  }
  .contact-social .social-dot {
    width: 12px;
    height: 12px;
    border-radius: 50%;
    background: var(--text-dark);
  }
  .contact-phone {
    margin: 10px 0 0;
    font-weight: 700;
    font-size: 32px;
    line-height: 1.1;
    color: var(--text-dark);
  }
</style>
</head>
<body>
<main class="canvas">
  <section class="wrap-panel" aria-label="Sunvale vehicle wrap side panel">
    <svg class="wrap-graphics" viewBox="0 0 1080 440" preserveAspectRatio="none">
      <defs>
        <linearGradient id="halftone-fade" x1="0" y1="1" x2="1" y2="0.1">
          <stop offset="0" stop-color="#9fcdf0" stop-opacity="0"/>
          <stop offset="0.35" stop-color="#9fcdf0" stop-opacity="0.5"/>
          <stop offset="0.75" stop-color="#5fb6ec" stop-opacity="0.7"/>
          <stop offset="1" stop-color="#2f9fe6" stop-opacity="0.85"/>
        </linearGradient>
      </defs>
      <path role="img" aria-label="Blue halftone dot texture sweeping up from the lower left to the rear"
            d="M300 440 C520 380 780 280 950 40 L990 0 L1080 0 L1080 440 Z"
            fill="url(#halftone-fade)"/>
      <path class="rear-band" d="M920 290 C980 270 1030 240 1080 205 L1080 440 L900 440 Z"
            fill="#2f9fe6"/>
    </svg>

    <div class="brand-block">
      <h1 class="brand-name">
        <span class="brand-dot" aria-hidden="true"></span>
        <span class="brand-wordmark">SUNVALE</span>
      </h1>
      <div class="contact-stack">
        <p class="contact-website">sunvale.bg</p>
        <p class="contact-social"><span class="social-dot" aria-hidden="true"></span>SunvaleBG</p>
      </div>
      <p class="contact-phone">+359 870 412 605</p>
    </div>
  </section>
</main>
</body>
</html>
```